Staffing/Recruitment company

We need to upgrade our website. At the moment we have a template that was built last year and looks not good at all.
We would like to update it with a new design based on what is popular this year. Including some visual effects etc.
This website is to give all information to our potential clients about what we do, clients with worked in the past, how to contact us and about us.
The website consists of 4 pages.
We would like to see a design that uses the color blue.
The current website is https://brightlanestaff.us/
Logo of the company is uploaded

Some designs were not complete...

```html
<!DOCTYPE html>
<html lang="en">
<head>
<meta charset="utf-8">
<title>Our Divisions – Brightlane Staffing</title>
<link href="https://fonts.googleapis.com/css2?family=Poppins:wght@400;500;600;700&family=Roboto:wght@300;400;500&display=swap" rel="stylesheet">
<style>
:root{
  --blue:#1f3f9a;
  --blue-link:#1f4fb3;
  --orange:#f05a28;
  --ink:#1b1b1b;
  --muted:#666;
  --header-bg:#f3f3f3;
  --line:#e4e4e4;
  --footer-bg:#232323;
  --footer-text:#8c8c8c;
  --footer-line:#363636;
  --white:#fff;
}
*{box-sizing:border-box;margin:0;padding:0}
html,body{width:802px;height:1200px;overflow:hidden}
body{position:relative;background:var(--white);font-family:'Roboto',sans-serif;color:var(--ink)}
.abs{position:absolute}

.topbar{left:0;top:0;width:802px;height:33px;background:var(--blue);color:var(--white);font-size:8.5px}
.topbar .promo{left:54px;top:11px}
.apply-btn{left:158px;top:9px;width:62px;height:15px;border-radius:8px;background:var(--orange);font:600 6.5px 'Poppins',sans-serif;letter-spacing:.5px;text-align:center;line-height:15px}
.toplinks{right:54px;top:11px;display:flex;gap:0}
.toplinks span{padding:0 7px;border-left:1px solid rgba(255,255,255,.25)}
.toplinks span:first-child{border-left:none}

.header{left:0;top:33px;width:802px;height:98px;background:var(--header-bg)}
.brand{left:54px;top:38px;display:flex;align-items:center;gap:5px;font:700 11.5px 'Poppins',sans-serif;color:var(--blue)}
.brand .mark{width:34px;height:34px;border:3px solid var(--blue)}
.contact{display:flex;gap:8px;align-items:center}
.contact .lbl{font:italic 300 8.5px 'Poppins',sans-serif;color:#888}
.contact .val{font:500 9.5px 'Poppins',sans-serif;color:var(--ink);margin-top:3px}
.c-addr{left:406px;top:57px}
.c-phone{left:529px;top:57px}
.join-btn{left:654px;top:57px;width:97px;height:29px;border:1px solid #ddd;border-radius:15px;font:600 8px 'Poppins',sans-serif;letter-spacing:.8px;text-align:center;line-height:27px}

.hero{left:0;top:131px;width:802px;height:205px;background:linear-gradient(90deg,#3a3f45,#5a5f63 35%,#2e3338 60%,#4d5258)}
.hero h1{position:absolute;left:0;right:0;top:85px;text-align:center;font:700 30px 'Poppins',sans-serif;color:var(--white)}

.nav{left:54px;top:110px;width:697px;height:42px;background:var(--white);display:flex;align-items:center;box-shadow:0 2px 8px rgba(0,0,0,.06)}
.nav ul{list-style:none;display:flex;padding-left:6px}
.nav li{font:600 8px 'Poppins',sans-serif;padding:0 13px;border-right:1px solid var(--line);position:relative}
.nav li.active{color:var(--orange)}
.nav li.active::after{content:"";position:absolute;left:50%;bottom:-7px;width:7px;height:1.5px;margin-left:-3px;background:var(--orange)}
.social-top{position:absolute;right:12px;top:15px;display:flex;align-items:center;gap:5px;font:300 8.5px 'Roboto',sans-serif;color:#555}
.social-top i{display:block;width:9px;height:9px;background:#777;border-radius:1px}

.crumbs{left:54px;top:349px;font-size:8.5px}
.crumbs .cur{color:var(--blue-link)}
.crumbs .sep{margin:0 6px;color:#888}
.crumb-line{left:54px;top:373px;width:697px;height:1px;background:var(--line)}

.division{width:220px;text-align:center}
.division .photo{width:220px;height:161px}
.division h2{font:400 15.5px 'Poppins',sans-serif;margin-top:14px}
.division p{font-size:8.5px;color:var(--blue-link);margin-top:5px}

.footer{left:0;top:902px;width:802px;height:298px;background:var(--footer-bg);color:var(--footer-text)}
.f-brand{left:54px;top:58px;display:flex;align-items:center;gap:5px;font:700 9.5px 'Poppins',sans-serif;color:var(--white)}
.f-brand .mark{width:26px;height:26px;border:2px solid var(--white)}
.f-head{font:400 13.5px 'Poppins',sans-serif;color:var(--white)}
.f-rule{height:1px;background:var(--footer-line);top:86px;width:230px}
.f-info{left:54px;top:128px;list-style:none;font:300 8.5px 'Roboto',sans-serif;line-height:17px}
.f-info li::before{content:"";display:inline-block;width:6px;height:6px;border-radius:50%;background:#777;margin-right:5px}
.f-links{list-style:none;font:300 8.5px 'Roboto',sans-serif;line-height:18.2px}
.f-links li::before{content:"›";margin-right:6px}
.f-news{left:530px;top:114px;width:225px;font:300 8.5px 'Roboto',sans-serif;line-height:16px}
.f-input{left:530px;top:154px;width:221px;height:30px;border:1px solid #555;display:flex;align-items:center;font-size:8.5px;color:#ccc}
.f-input .env{width:25px;height:100%;border-right:1px solid #444;display:flex;align-items:center;justify-content:center}
.f-input .txt{flex:1;padding-left:8px}
.f-input .send{width:27px;border-left:1px solid #444;height:16px;display:flex;align-items:center;justify-content:center}
.f-social{left:530px;top:202px;display:flex;gap:11px}
.f-social i{display:block;width:26px;height:26px;border:1px solid #444;border-radius:50%}
.f-bottom{left:0;top:258px;width:802px;height:1px;background:var(--footer-line)}
.copyright{left:54px;top:273px;font:300 8.5px 'Roboto',sans-serif}
</style>
</head>
<body>

<div class="abs topbar">
  <span class="abs promo">Looking for a dream job?</span>
  <span class="abs apply-btn">APPLY NOW</span>
  <div class="abs toplinks"><span>Get Support</span><span>Job Career</span><span>Feedbacks</span><span>English ˅</span></div>
</div>

<div class="abs header"></div>
<div class="abs brand"><span class="mark"></span>BRIGHTLANE STAFFING</div>
<div class="abs contact c-addr">
  <svg width="14" height="18" viewBox="0 0 14 18"><path d="M7 1a6 6 0 0 1 6 6c0 4-6 10-6 10S1 11 1 7a6 6 0 0 1 6-6z" fill="none" stroke="#1f3f9a" stroke-width="1.2"/><circle cx="7" cy="7" r="2" fill="none" stroke="#1f3f9a" stroke-width="1.2"/></svg>
  <div><div class="lbl">4820 Elm Street</div><div class="val">Arlington, VA, USA</div></div>
</div>
<div class="abs contact c-phone">
  <svg width="18" height="18" viewBox="0 0 18 18"><path d="M3 2l3 0 1.5 4-2 1.5a9 9 0 0 0 5 5l1.5-2 4 1.5v3a2 2 0 0 1-2 2A14 14 0 0 1 1 4a2 2 0 0 1 2-2z" fill="none" stroke="#1f3f9a" stroke-width="1.2"/><path d="M11 2a5 5 0 0 1 5 5M11 5a2 2 0 0 1 2 2" fill="none" stroke="#1f3f9a" stroke-width="1.2"/></svg>
  <div><div class="lbl">Quick Contact:</div><div class="val">+1 555 010 4477</div></div>
</div>
<div class="abs join-btn">JOIN NOW</div>

<div class="abs hero" role="img" aria-label="Collage of office teams, handshakes and laptops"><h1>Our Divisions</h1></div>

<nav class="abs nav">
  <ul>
    <li>HOME</li><li class="active">ABOUT US</li><li>SERVICES</li><li>CLIENTS</li><li>SOLUTIONS</li><li>JOIN US</li><li>CONTACT US</li>
  </ul>
  <div class="social-top">STAY CONNECTED: <i></i><i></i><i></i><i></i></div>
</nav>

<div class="abs crumbs">Home<span class="sep">›</span><span class="cur">Our Divisions</span></div>
<div class="abs crumb-line"></div>

<div class="abs division" style="left:54px;top:421px">
  <div class="photo" role="img" aria-label="Glass skyscrapers against a blue sky" style="background:linear-gradient(160deg,#2b3a45,#8aa0b3 55%,#3d4d58)"></div>
  <h2>Finance</h2><p>Banking and Insurance</p>
</div>
<div class="abs division" style="left:292px;top:421px">
  <div class="photo" role="img" aria-label="IT staff working at monitors in an operations room" style="background:linear-gradient(160deg,#1f3d55,#3f6c86 50%,#243241)"></div>
  <h2>Information Technology</h2><p>Small and Medium Enterprises</p>
</div>
<div class="abs division" style="left:530px;top:421px">
  <div class="photo" role="img" aria-label="Doctor holding a tablet with medical icons" style="background:linear-gradient(160deg,#c8dcec,#eef3f7 55%,#d8c4b4)"></div>
  <h2>Healthcare</h2><p>Hospitals, Clinics, and Physician Practices</p>
</div>
<div class="abs division" style="left:54px;top:651px">
  <div class="photo" role="img" aria-label="Capitol building with a waving flag" style="background:linear-gradient(160deg,#2a3e7a,#c4cfe0 45%,#b83a3a 60%,#4f8a3a)"></div>
  <h2>Government Projects</h2><p>Financial Management and Project Management</p>
</div>
<div class="abs division" style="left:292px;top:651px">
  <div class="photo" role="img" aria-label="Desk with laptop, papers, coffee and calculator" style="background:linear-gradient(160deg,#4a3a2e,#7a634f 50%,#3b2e24)"></div>
  <h2>Miscellaneous</h2><p>Education, NGOs and Logistics</p>
</div>

<footer class="abs footer">
  <div class="abs f-brand"><span class="mark"></span>BRIGHTLANE STAFFING</div>
  <div class="abs f-rule" style="left:54px"></div>
  <ul class="abs f-info">
    <li>Address: 4820 Elm St, Arlington, VA</li>
    <li>Phone: +1 555 010 2290</li>
    <li>Email: hello@brightlanemail.com</li>
    <li>Mon to Sat: 9.00 am to 5:00 pm</li>
  </ul>

  <div class="abs f-head" style="left:292px;top:54px">Quick Links</div>
  <div class="abs f-rule" style="left:292px"></div>
  <ul class="abs f-links" style="left:292px;top:109px"><li>Home</li><li>About Us</li><li>Services</li><li>Clients</li><li>Solutions</li><li>Contact Us</li></ul>
  <ul class="abs f-links" style="left:411px;top:109px"><li>Join Us</li><li>FAQs</li><li>Testimonials</li><li>Job Career</li><li>Meet Our Team</li><li>Privacy Policy</li></ul>

  <div class="abs f-head" style="left:530px;top:54px">Newsletter</div>
  <div class="abs f-rule" style="left:530px"></div>
  <p class="abs f-news">Sign up today for get hints, tips, latest updates &amp; news of Brightlane Staffing LLC.</p>
  <div class="abs f-input">
    <span class="env"><svg width="9" height="7" viewBox="0 0 9 7"><rect x=".5" y=".5" width="8" height="6" fill="none" stroke="#aaa"/><path d="M.5.5l4 3 4-3" fill="none" stroke="#aaa"/></svg></span>
    <span class="txt">Email Addres...</span>
    <span class="send"><svg width="10" height="10" viewBox="0 0 10 10"><path d="M0 5L10 0 7 10 5 6z" fill="#bbb"/></svg></span>
  </div>
  <div class="abs f-social"><i></i><i></i><i></i><i></i></div>
  <div class="abs f-bottom"></div>
  <div class="abs copyright">Copyrights © 2022 Brightlane Staffing LLC. All Rights Reserved.</div>
</footer>

</body>
</html>
```